AMBER AND STONE WEB

We need a home design in wordpress, we have now a web but we would like to improve it. Our current web is www.amberandstonevillas.example Our business is holliday rental of villas in Ibiza. Our guest must know that we are a reliable company, professional and with experience and good reviews. We want them to click in our reservation engine: https://bookings.amberandstonevillas.example/en/ and make reservation in our website. We would also like to say that all the properties that we have are just us who commercialize so we have best price available. Many people are going to see our villas in staylister.example and look to our website to make a reservation with us so we need to show them that they are at the right place and click at our link to our reservation engine. What make us special is that we are a local company, we are from Ibiza, Our guests are always received in person by the Amber and Stone Villas team. You will enjoy extensive tourist information when you check in and during the entire stay. You will be attended by ChatLoop and calls, always happy to help so that you have a happy and fun stay! Our guest stay is better than in hotel as they have more spece, private swiming pool, private garden, barbeque ... To rent a villa is the best way to stay in Ibiza. We also have a promotional video: https://vidshare.example/Qm7tLp2Xz9A Let our philosophy be shown, we think that coming on holiday to Ibiza implies seeing the nature that we have in Ibiza, hence our name AMBER AND STONE, like the pins that almost touch the sea in Ibiza, or the posidonea meadows where the intense green of the seaweed and the blue of the sea. We are aware of the environment, and we love Ibiza. For us, the client who visits Ibiza, should rent a car, go around the island, eat in a restaurant one day in front of the sea, is a night of partying to the discs, go shopping, visit the ancient heritage of Umanity, make some aquatic sport, enjoy the pool, those are for us Ibiza.

Target Market(s)

Europe, people from Holand, UK, Germany, France, Spain ...

Industry/Entity Type

Tourism

Colors

Designer to choose colors to be used in the design.

Requirements
Must have
• Pictures of Ibiza.
Nice to have
• Our name Amber and Stone Villas is beacuse in Ibiza there is forest that almost touch the watter of the Mediterranean sea, so you can see green of the forest and blue of the sea and the sky. And also beacause under the watter of the sea there is a plant called Posidonia that is also green please see the picture of posidonia.

```html
<!DOCTYPE html>
<html lang="en">
<head>
<meta charset="utf-8">
<title>Amber and Stone Villas – Holiday Villas in Ibiza</title>
<link href="https://fonts.googleapis.com/css2?family=Montserrat:wght@400;600;700;800&family=Open+Sans:wght@400;600&family=Roboto+Slab:wght@600;700&display=swap" rel="stylesheet">
<style>
:root{
  --green:#8cc63f;
  --blue:#29b3e6;
  --navy:#0c1a2b;
  --navy-deep:#081320;
  --ink:#222;
  --muted:#8a8a8a;
  --line:#e3e3e3;
  --white:#fff;
  --sea:#1c8fc0;
}
*{box-sizing:border-box;margin:0;padding:0}
html,body{width:1200px;height:2192px;overflow:hidden}
body{font-family:"Open Sans",sans-serif;color:var(--ink);background:var(--white);font-size:13px;position:relative}
.btn{display:inline-block;background:linear-gradient(90deg,var(--green),var(--blue));color:var(--white);font-family:"Montserrat",sans-serif;font-weight:600;font-size:13px;padding:10px 22px;border-radius:3px;text-decoration:none}
.btn--green{background:var(--green)}
.btn--blue{background:var(--blue)}

/* header */
.site-header{position:absolute;top:0;left:0;width:1200px;height:64px;background:var(--white);display:flex;align-items:center;padding:0 100px;z-index:3}
.brand{display:flex;align-items:center;gap:10px;font-family:"Montserrat",sans-serif;font-weight:700;font-size:15px;color:var(--green);text-decoration:none}
.brand__dot{width:24px;height:24px;border-radius:50%;background:var(--green)}
.main-nav{display:flex;gap:36px;margin-left:150px;font-family:"Montserrat",sans-serif;font-size:13px;font-weight:600}
.main-nav a{color:var(--ink);text-decoration:none}
.lang{width:22px;height:14px;background:linear-gradient(#c8102e 0 33%,#fff 33% 66%,#012169 66%);margin-left:26px}
.header-actions{margin-left:auto;display:flex;gap:10px}
.header-actions .btn{padding:8px 16px;font-size:12px}

/* hero */
.hero{position:absolute;top:64px;left:0;width:1200px;height:366px;background:linear-gradient(180deg,#6fb6d6 0%,#2a8fb8 45%,#186f8c 70%,#3b6a3a 100%);text-align:center;color:var(--white)}
.hero__title{font-family:"Montserrat",sans-serif;font-weight:800;font-size:38px;letter-spacing:1px;margin-top:130px;text-shadow:0 2px 6px rgba(0,0,0,.35)}
.hero__text{font-size:14px;width:560px;margin:12px auto 18px;line-height:1.5}

/* search */
.search{position:absolute;top:430px;left:0;width:1200px;height:70px;background:#f4f4f4;display:flex;align-items:center;justify-content:center;gap:10px}
.search__field{height:40px;background:var(--white);border:1px solid var(--line);color:var(--muted);font-size:12px;display:flex;align-items:center;padding:0 14px;gap:8px}
.search__field--wide{width:430px}
.search__field--mid{width:190px}
.search__field--short{width:150px}
.search .btn{height:40px;padding:11px 34px}

/* features */
.features{position:absolute;top:540px;left:140px;width:920px;display:flex;justify-content:space-between}
.feature{display:flex;gap:14px;width:270px}
.feature__icon{width:56px;height:56px;flex:none}
.feature h3{font-family:"Montserrat",sans-serif;font-size:13px;font-weight:700;margin-bottom:6px}
.feature p{font-size:11px;color:var(--muted);line-height:1.5}

/* destinations */
.section-title{font-family:"Montserrat",sans-serif;font-weight:700;font-size:24px;text-align:center}
.section-sub{font-size:12px;color:var(--muted);text-align:center;margin-top:6px}
.destinations{position:absolute;top:770px;left:0;width:1200px}
.cards{display:flex;gap:28px;justify-content:center;margin-top:34px}
.card{width:214px;text-align:center}
.card__img{height:236px}
.card h3{font-family:"Roboto Slab",serif;font-size:15px;font-weight:700;margin:20px 8px 12px;line-height:1.35}
.card p{font-size:11px;color:var(--muted);line-height:1.5;padding:0 10px}

/* offer */
.offer{position:absolute;top:1345px;left:0;width:1200px;height:270px;display:flex}
.offer__promo{width:600px;background:linear-gradient(90deg,#0f5f86,#1f8fbf);color:var(--white);display:flex;align-items:center;padding-left:200px;gap:22px}
.offer__badge{font-family:"Montserrat",sans-serif;font-weight:800;line-height:.95}
.offer__badge .pct{font-size:40px;color:var(--white)}
.offer__badge .off{font-size:16px}
.offer__badge .sale{font-size:36px;display:block}
.offer__copy h2{font-family:"Montserrat",sans-serif;font-weight:800;font-size:26px;line-height:1.1}
.offer__copy p{font-size:11px;line-height:1.5;margin:10px 0 14px;width:200px}
.offer__video{width:600px;background:linear-gradient(135deg,#1c1c1c,#3a3a3a 60%,#5c4a3e);position:relative;color:var(--white)}
.video__bar{position:absolute;top:14px;left:18px;right:18px;display:flex;align-items:center;gap:10px;font-size:14px}
.video__bar span{width:28px;height:28px;border-radius:50%;background:var(--green);flex:none}
.video__play{position:absolute;left:274px;top:110px;width:54px;height:38px;border-radius:8px;background:#d22}
.video__caption{position:absolute;left:150px;bottom:22px;width:300px;text-align:center;font-family:"Montserrat",sans-serif;font-weight:800;font-size:17px;background:rgba(0,0,0,.75);padding:6px 8px;line-height:1.3}

/* why + testimonials */
.about{position:absolute;top:1660px;left:140px;width:920px;display:flex;gap:60px}
.about h2{font-family:"Montserrat",sans-serif;font-weight:700;font-size:20px;margin-bottom:14px}
.why{width:430px}
.why p{font-size:11px;color:var(--muted);line-height:1.6;margin-bottom:10px}
.reviews{width:430px;text-align:center}
.review__name{font-size:10px;font-weight:600;color:var(--muted);letter-spacing:1px}
.review__photo{width:58px;height:58px;border-radius:50%;background:#c9c9c9;margin:8px auto 10px}
.review{display:flex;align-items:center;gap:12px}
.review__quote{font-family:"Roboto Slab",serif;font-size:30px;color:var(--blue)}
.review p{font-size:11px;color:var(--muted);line-height:1.6;font-style:italic}
.dots{display:flex;justify-content:center;gap:6px;margin-top:14px}
.dots i{width:8px;height:8px;border-radius:50%;background:var(--line)}
.dots i.on{background:var(--green)}

/* footer */
.site-footer{position:absolute;top:1990px;left:0;width:1200px;height:202px;background:var(--navy);color:#c5ccd6}
.footer__cols{display:flex;padding:30px 100px 0;gap:40px}
.footer__col h4{font-family:"Montserrat",sans-serif;color:var(--white);font-size:12px;font-weight:700;margin-bottom:12px}
.footer__col ul{list-style:none;font-size:10px;line-height:1.75}
.footer__brand{width:260px}
.footer__brand .brand{color:var(--white);margin-bottom:12px}
.footer__brand p{font-size:10px;line-height:1.6}
.socials{display:flex;gap:8px;margin-top:12px}
.socials i{width:20px;height:20px;border-radius:50%;border:1px solid #6b7a8c}
.contact li{display:flex;gap:8px;align-items:flex-start}
.contact svg{flex:none;margin-top:2px}
.footer__bar{position:absolute;bottom:0;left:0;width:100%;height:20px;background:var(--navy-deep);font-size:9px;padding:4px 100px;color:#7e8a99}
</style>
</head>
<body>

<header class="site-header">
  <a class="brand" href="#"><span class="brand__dot"></span>Amber and Stone</a>
  <nav class="main-nav">
    <a href="#">Home</a><a href="#">Experience</a><a href="#">About Us</a><a href="#">Contact Us</a>
  </nav>
  <span class="lang" role="img" aria-label="Language selector"></span>
  <div class="header-actions">
    <a class="btn btn--green" href="#">All Properties</a>
    <a class="btn btn--blue" href="#">Book Now</a>
  </div>
</header>

<section class="hero" role="img" aria-label="Photo of an Ibiza bay with pine forest touching the turquoise sea">
  <h1 class="hero__title">THE BEST WAY TO LIVE IN IBIZA</h1>
  <p class="hero__text">Private villas with pool and garden, welcomed in person by our local team. Book direct for the best price on the island.</p>
  <a class="btn" href="#">Book Now</a>
</section>

<form class="search">
  <div class="search__field search__field--wide">
    <svg width="14" height="14" viewBox="0 0 14 14"><rect x="1" y="2" width="12" height="11" fill="none" stroke="#999"/><line x1="1" y1="5" x2="13" y2="5" stroke="#999"/></svg>Check in – Check out</div>
  <div class="search__field search__field--mid">Number of guests</div>
  <div class="search__field search__field--short">Bedrooms</div>
  <a class="btn" href="#">Search</a>
</form>

<section class="features">
  <div class="feature">
    <svg class="feature__icon" viewBox="0 0 56 56"><path d="M28 6c-9 0-16 7-16 16 0 12 16 28 16 28s16-16 16-28c0-9-7-16-16-16z" fill="none" stroke="#444" stroke-width="2"/><circle cx="28" cy="22" r="6" fill="none" stroke="#444" stroke-width="2"/></svg>
    <div><h3>TOP DESTINATION</h3><p>A small team welcomes every guest and shares tips for the whole stay.</p></div>
  </div>
  <div class="feature">
    <svg class="feature__icon" viewBox="0 0 56 56"><path d="M8 28 28 8h18v18L26 46z" fill="none" stroke="#444" stroke-width="2"/><circle cx="38" cy="16" r="3" fill="none" stroke="#444" stroke-width="2"/></svg>
    <div><h3>THE BEST PRICES</h3><p>Only we offer these villas, so booking here is always the best rate.</p></div>
  </div>
  <div class="feature">
    <svg class="feature__icon" viewBox="0 0 56 56"><path d="M10 44h36M14 44V30h28v14M20 30V18h16v12M24 18V10h8v8" fill="none" stroke="#444" stroke-width="2"/></svg>
    <div><h3>AMAZING SERVICES</h3><p>Help by chat and calls every day so your holiday is happy and fun.</p></div>
  </div>
</section>

<section class="destinations">
  <h2 class="section-title">MOST POPULAR DESTINATIONS IN IBIZA</h2>
  <p class="section-sub">Hand picked places our guests love to visit during their stay</p>
  <div class="cards">
    <article class="card">
      <div class="card__img" role="img" aria-label="Photo of a rental car on a coastal road" style="background:linear-gradient(160deg,#5aa9d8,#2f6f9a 60%,#6b8f4a)"></div>
      <h3>Luxurious Car Rental Service Available</h3>
      <p>A small river named Duden flows by their place and supplies it.</p>
    </article>
    <article class="card">
      <div class="card__img" role="img" aria-label="Photo of a harbour with boats and white houses" style="background:linear-gradient(160deg,#9ccbe4,#d9c8a8 55%,#2c86b4)"></div>
      <h3>Cruise Private Party Booking Available</h3>
      <p>A small river named Duden flows by their place and supplies it.</p>
    </article>
    <article class="card">
      <div class="card__img" role="img" aria-label="Photo of a seafood dish" style="background:linear-gradient(160deg,#e3c8a1,#b9783f 55%,#7a4a2a)"></div>
      <h3>Tremendous Options for Food Lovers</h3>
      <p>A small river named Duden flows by their place and supplies it.</p>
    </article>
    <article class="card">
      <div class="card__img" role="img" aria-label="Photo of a villa swimming pool" style="background:linear-gradient(160deg,#bfe6f5,#3ab6e0 55%,#1b7ea8)"></div>
      <h3>Luxurious Swimming Pools Available</h3>
      <p>A small river named Duden flows by their place and supplies it.</p>
    </article>
  </div>
</section>

<section class="offer">
  <div class="offer__promo">
    <div class="offer__badge"><span class="pct">45%</span><span class="off"> OFF</span><span class="sale">SALE</span></div>
    <div class="offer__copy">
      <h2>JUST HURRY UP<br>LIMITED OFFER!</h2>
      <p>Book your villa directly with us for the best price and a warm local welcome.</p>
      <a class="btn btn--green" href="#">Book Now</a>
    </div>
  </div>
  <div class="offer__video" role="img" aria-label="Promotional video still of Ibiza">
    <div class="video__bar"><span></span>¡Aquí es has visto esto aún en Ibiza!</div>
    <div class="video__play"></div>
    <div class="video__caption">MORE THAN A PARTY ISLAND!<br>LIVE THE REAL EXPERIENCE OF IBIZA!</div>
  </div>
</section>

<section class="about">
  <div class="why">
    <h2>WHY CHOOSE US</h2>
    <p>Amber and Stone Villas is a local company from Ibiza offering holiday villas where the forest almost touches the sea. All our properties are marketed only by us, so you always get the best price.</p>
    <p>Every guest is received in person and gets plenty of tourist tips at check in and during the stay. Villas have more space than a hotel, with private pool, garden and barbecue.</p>
    <a class="btn" href="#">Read More</a>
  </div>
  <div class="reviews">
    <h2>OUR SATISFIED GUESTS SAYS</h2>
    <div class="review__name">MARCO ELLISON</div>
    <div class="review__photo" role="img" aria-label="Guest portrait"></div>
    <div class="review">
      <span class="review__quote">“</span>
      <p>Wonderful villa, spotless pool and a lovely team who met us at the door and helped with every plan. We will book again next summer for sure.</p>
      <span class="review__quote">”</span>
    </div>
    <div class="dots"><i class="on"></i><i></i><i></i></div>
  </div>
</section>

<footer class="site-footer">
  <div class="footer__cols">
    <div class="footer__col footer__brand">
      <a class="brand" href="#"><span class="brand__dot"></span>Amber and Stone</a>
      <p>Holiday villas in Ibiza run by a local team. Private pools, gardens and a personal welcome for every guest.</p>
      <div class="socials"><i></i><i></i><i></i><i></i></div>
    </div>
    <div class="footer__col" style="width:180px">
      <h4>INFORMATION</h4>
      <ul><li>About</li><li>Services</li><li>Terms and Conditions</li><li>Become a partner</li><li>Best Price Guarantee</li><li>Privacy and Policy</li></ul>
    </div>
    <div class="footer__col" style="width:200px">
      <h4>CUSTOMER SUPPORT</h4>
      <ul><li>FAQ</li><li>Payment Option</li><li>Booking Tips</li><li>How it works</li><li>Contact Us</li><li>Holiday Information</li></ul>
    </div>
    <div class="footer__col" style="width:240px">
      <h4>HAVE A QUESTION ?</h4>
      <ul class="contact">
        <li><svg width="10" height="12" viewBox="0 0 10 12"><path d="M5 0a4 4 0 0 0-4 4c0 3 4 8 4 8s4-5 4-8a4 4 0 0 0-4-4z" fill="#c5ccd6"/></svg>18 Harbour Lane, Santa Vella, Ibiza, Spain</li>
        <li><svg width="10" height="10" viewBox="0 0 10 10"><path d="M2 0 4 3 3 4c1 2 2 3 3 3l1-1 3 2-1 2C5 10 0 5 0 1z" fill="#c5ccd6"/></svg>+34 900 555 017</li>
        <li><svg width="11" height="8" viewBox="0 0 11 8"><rect width="11" height="8" fill="#c5ccd6"/><path d="M0 0l5.5 4L11 0" stroke="#0c1a2b" fill="none"/></svg>reservas@amberandstonevillas.example</li>
      </ul>
    </div>
  </div>
  <div class="footer__bar">© 2024 All rights reserved</div>
</footer>

</body>
</html>
```